Poster Design with Yoga Foam Roller Exercise Guide

Hi there!
We are looking for a poster design for our yoga foam roller product.
1. Foam roller.jpg shows our product. The poster is going to be wrapped around the roller
2. Poster dimensions: 42x28.5cm.
3. Design style matches our reference box.png and reference flat.png (colors, typefaces, overall look & feel)
4. Also check reference poster.jpg as a reference design for use of colors and overall look & feel
5. Written instructions are to be taken from written instructions.pdf
6. Illustrations are to be taken from illustrations.zip
7. Also use illustrations #2, 3 and 8 from girls.jpg, but add faces and change girl's hair (according to hair.jpg)
8. please see "orchard pals. jpg" for the ambience of the colours (instead of green, please use a brown colour). the base colours must be plain, without grain.
9. Please also create a small label design (53x17mm, to be inserted into a socket in the foam roller, see label.jpg). Please use our logo (reference box/reference flat/logo.jpg) and/or „Velvet Harbor“ as text as you see fit.
Thank you very much, we are really excited about receiving your designs :)

```html
<!DOCTYPE html>
<html lang="de">
<head>
<meta charset="utf-8">
<title>Übungsbeispiele – Exercise Guide</title>
<link href="https://fonts.googleapis.com/css2?family=Montserrat:wght@400;500;700&family=Quicksand:wght@500;600&display=swap" rel="stylesheet">
<style>
  :root{
    --band:#f0d9c6;
    --panel:#fdfaf0;
    --ink:#6b563f;
    --body:#a07f60;
    --figure-light:#efe0cd;
    --figure-mid:#dcc3a5;
    --figure-deep:#b89574;
    --label-dark:#1c1511;
    --label-mid:#4a3320;
    --gold:#e0a858;
    --page:#ffffff;
  }
  *{margin:0;padding:0;box-sizing:border-box}
  html,body{width:1200px;height:1047px;overflow:hidden;background:var(--page)}
  .canvas{position:relative;width:1200px;height:1047px;font-family:"Montserrat",sans-serif}

  .poster{position:absolute;left:0;top:0;width:1200px;height:814px;background:var(--band)}
  .poster-panel{position:absolute;left:18px;top:14px;width:1164px;height:652px}
  .poster-panel svg{position:absolute;left:0;top:0}

  .figure{position:absolute;border-radius:14px;
    background:linear-gradient(160deg,var(--figure-light) 0%,var(--figure-mid) 60%,var(--figure-deep) 100%)}

  .exercise{position:absolute;color:var(--body);font-size:6.4px;line-height:1.32;font-weight:500}
  .lang{display:flex;gap:6px;margin-bottom:8px}
  .lang-code{font-weight:700;color:var(--ink);font-size:10.5px;line-height:1;min-width:17px}
  .lang-text h3{font-weight:700;color:var(--ink);font-size:8.2px;letter-spacing:1.9px;margin-bottom:2px;line-height:1.15}
  .side .lang{display:block;margin-bottom:9px}
  .side .lang-code{display:block;margin-bottom:5px}

  .brand-mark{position:absolute;left:36px;top:724px;display:flex;align-items:center;gap:8px;font-family:"Quicksand",sans-serif;font-weight:600;font-size:22px;color:var(--ink)}
  .brand-mark .dot{width:14px;height:14px;border-radius:50%;background:var(--ink)}

  .title{position:absolute;right:32px;top:668px;text-align:right;font-family:"Quicksand",sans-serif;color:var(--ink);font-weight:500}
  .title .de{font-size:70px;line-height:1;letter-spacing:1px}
  .title .en{font-size:38px;line-height:1;margin-top:4px;letter-spacing:.5px}

  .label{position:absolute;left:338px;top:844px;width:515px;height:164px;background:radial-gradient(ellipse 45% 70% at 50% 45%,var(--label-mid) 0%,var(--label-dark) 85%);display:flex;align-items:center;justify-content:center}
  .label-name{font-family:"Quicksand",sans-serif;font-weight:600;font-size:28px;color:var(--gold);letter-spacing:1px}
</style>
</head>
<body>
<div class="canvas">
  <section class="poster">
    <div class="poster-panel">
      <svg width="1164" height="652" viewBox="0 0 1164 652" aria-hidden="true">
        <path fill="#fdfaf0" d="M0 0H1164V642C1120 646 1090 640 1040 644C990 648 960 640 900 643C850 646 810 641 760 645C700 648 660 640 600 644C540 647 500 641 440 645C380 648 340 641 280 644C220 647 180 640 120 645C70 648 40 641 0 643Z"/>
      </svg>
    </div>

    <!-- row 1 -->
    <div class="figure" style="left:30px;top:128px;width:224px;height:76px" role="img" aria-label="Illustration: Mann liegt seitlich auf der Schaumstoffrolle"></div>
    <div class="exercise" style="left:44px;top:215px;width:212px">
      <div class="lang"><span class="lang-code">DE</span><div class="lang-text"><h3>SEITLICHER RÜCKEN</h3>Seitlich auf die Rolle legen, mit dem oberen Arm abstützen. Vom unteren Rücken bis zur Achsel vor- und zurückrollen.</div></div>
      <div class="lang"><span class="lang-code">EN</span><div class="lang-text"><h3>LATERAL BACK</h3>Lie down laterally on the foam roller, using the other arm as support. Then roll back and forth from the lower back to the armpit.</div></div>
    </div>

    <div class="figure" style="left:284px;top:128px;width:224px;height:68px" role="img" aria-label="Illustration: Frau liegt bäuchlings mit der Rolle unter den Oberschenkeln"></div>
    <div class="exercise" style="left:296px;top:215px;width:206px">
      <div class="lang"><span class="lang-code">DE</span><div class="lang-text"><h3>VORDERER OBERSCHENKEL</h3>Bäuchlings auf die Rolle legen und unter die vorderen Oberschenkel positionieren. Mit den Armen abstützen. Gleichmäßig vor- und zurückrollen.</div></div>
      <div class="lang"><span class="lang-code">EN</span><div class="lang-text"><h3>FRONT OF UPPER THIGHS</h3>Lying on the belly, position the roller under the quads. Use arms as support. Then roll back and forth, massaging the whole front of the upper thighs.</div></div>
    </div>

    <div class="figure" style="left:534px;top:124px;width:180px;height:76px" role="img" aria-label="Illustration: Frau mit oberem Rücken auf der Rolle"></div>
    <div class="exercise" style="left:534px;top:215px;width:196px">
      <div class="lang"><span class="lang-code">DE</span><div class="lang-text"><h3>OBERER RÜCKEN</h3>Mit dem oberen Rücken auf die Rolle legen. Vom Steißbein bis zur Schulter mit angewinkelten Beinen vor- und zurückrollen. Dabei den Bauch fest anspannen und bei Bedarf den Kopf abstützen.</div></div>
      <div class="lang"><span class="lang-code">EN</span><div class="lang-text"><h3>UPPER BACK</h3>Lie down with the upper back on the roller. With angled legs, roll back and forth, keeping your stomach muscles under tension. Support your head with your hands if necessary.</div></div>
    </div>

    <div class="figure" style="left:752px;top:76px;width:176px;height:120px" role="img" aria-label="Illustration: Mann sitzt mit dem Gesäß auf der Rolle"></div>
    <div class="exercise" style="left:750px;top:215px;width:198px">
      <div class="lang"><span class="lang-code">DE</span><div class="lang-text"><h3>GESÄß</h3>Auf die Rolle setzen, seitlich mit den Händen abstützen. Durch Bewegung der angewinkelten Beine Gesäß durch gleichmäßiges vor- und zurückrollen massieren.</div></div>
      <div class="lang"><span class="lang-code">EN</span><div class="lang-text"><h3>BUTTOCK</h3>Sit on the roller, supporting yourself with your hands. By changing the angle of your legs, move back and forth on the roller, massaging your buttocks.</div></div>
    </div>

    <div class="figure" style="left:964px;top:84px;width:84px;height:196px" role="img" aria-label="Illustration: Mann steht seitlich mit der Rolle an der Wand"></div>
    <div class="exercise side" style="left:1056px;top:110px;width:116px">
      <div class="lang"><span class="lang-code">DE</span><div class="lang-text"><h3>SCHULTERN (STEHEND)</h3>Seitlich an die Wand stellen, leicht in die Knie gehen. Rolle zwischen Schultern und Wand einklemmen. Rolle auf- und abbewegen, indem Sie abwechselnd in die Knie gehen und die Beine strecken.</div></div>
      <div class="lang"><span class="lang-code">EN</span><div class="lang-text"><h3>SHOULDERS (STANDING)</h3>Stand sideways on a wall with slightly bended knees, roller between your shoulder and the wall. Roll up and down by alternately kneeling and stretching your legs.</div></div>
    </div>

    <!-- row 2 -->
    <div class="figure" style="left:52px;top:348px;width:188px;height:136px" role="img" aria-label="Illustration: Mann sitzt mit der Rolle unter einem Oberschenkel"></div>
    <div class="exercise" style="left:50px;top:493px;width:206px">
      <div class="lang"><span class="lang-code">DE</span><div class="lang-text"><h3>HINTERER OBERSCHENKEL</h3>Auf den Boden setzen, Rolle unter einen der Oberschenkel legen. Mit beiden Armen abstützen, Gesäß anheben. Mit dem Oberschenkel gleichmäßig vor- und zurückrollen. Danach Seite wechseln und wiederholen.</div></div>
      <div class="lang"><span class="lang-code">EN</span><div class="lang-text"><h3>BACK OF UPPER THIGHS</h3>Sit on the ground, place the roller under one of your thighs, supporting yourself with both arms. Raise your buttocks and roll back and forth over your thigh evenly. Switch side and repeat.</div></div>
    </div>

    <div class="figure" style="left:284px;top:348px;width:188px;height:136px" role="img" aria-label="Illustration: Mann sitzt mit der Rolle unter der Wade"></div>
    <div class="exercise" style="left:278px;top:493px;width:206px">
      <div class="lang"><span class="lang-code">DE</span><div class="lang-text"><h3>WADEN</h3>Auf den Boden setzen, Rolle liegt quer unter der Wade. Mit beiden Händen und dem freien Bein abstützen. Wade gleichmäßig vor- und zurückrollen. Bauch, Rücken und Po bleiben dabei angespannt.</div></div>
      <div class="lang"><span class="lang-code">EN</span><div class="lang-text"><h3>CALVES</h3>Sit on the ground, roller placed under one calf. Support yourself with both hands and the other leg. Roll back and forth evenly while abdomen and back muscles remain tense.</div></div>
    </div>

    <div class="figure" style="left:506px;top:392px;width:206px;height:88px" role="img" aria-label="Illustration: Frau liegt seitlich mit dem Oberschenkel auf der Rolle"></div>
    <div class="exercise" style="left:510px;top:493px;width:206px">
      <div class="lang"><span class="lang-code">DE</span><div class="lang-text"><h3>SEITLICHER OBERSCHENKEL</h3>Mit einem Oberschenkel seitlich auf die Rolle legen, mit Armen abstützen. Das andere Bein vor sich auf den Boden stellen. Oberschenkel von der Hüfte bis zum Knie vor- und zurückrollen. Danach Seite wechseln und wiederholen.</div></div>
      <div class="lang"><span class="lang-code">EN</span><div class="lang-text"><h3>LATERAL THIGHS</h3>Lie down laterally on the roller, supporting yourself with both arms. Position the other leg in front of you. Evenly move your thigh back and forth from hip to knee. Switch side and repeat.</div></div>
    </div>

    <div class="figure" style="left:746px;top:404px;width:198px;height:72px" role="img" aria-label="Illustration: Mann liegt bäuchlings mit der Oberschenkelinnenseite auf der Rolle"></div>
    <div class="exercise" style="left:754px;top:493px;width:206px">
      <div class="lang"><span class="lang-code">DE</span><div class="lang-text"><h3>OBERSCHENKEL-INNENSEITE</h3>Auf den Bauch legen, mit abgewinkelten Armen abstützen. Ein Bein Richtung Schulter anwinkeln. Oberschenkelinnenseite auf die Rolle legen und vom Knie bis zum Becken vor- und zurückrollen.</div></div>
      <div class="lang"><span class="lang-code">EN</span><div class="lang-text"><h3>INSIDE OF UPPER THIGHS</h3>Lay on the belly, supporting yourself with angled arms. Bend one leg toward the shoulder and place the inner thigh on the roller. Roll back and forth from knee to pelvis.</div></div>
    </div>

    <div class="figure" style="left:972px;top:390px;width:76px;height:186px" role="img" aria-label="Illustration: Mann steht mit dem Rücken und der Rolle an der Wand"></div>
    <div class="exercise side" style="left:1054px;top:400px;width:118px">
      <div class="lang"><span class="lang-code">DE</span><div class="lang-text"><h3>OBERER RÜCKEN (STEHEND)</h3>Mit leicht angewinkelten Knien vor eine Wand stellen, Rolle zwischen Rücken und Wand auf Höhe der Schulterblätter einklemmen. Rolle auf- und abbewegen, indem Sie abwechselnd in die Knie gehen und die Beine strecken.</div></div>
      <div class="lang"><span class="lang-code">EN</span><div class="lang-text"><h3>UPPER BACK (STANDING)</h3>Position yourself in front of a wall with your knees slightly bent, roller between your back and the wall at the level of the shoulder blades. Roll up and down by alternately kneeling and stretching your legs.</div></div>
    </div>

    <div class="brand-mark"><span class="dot"></span>Velvet Harbor</div>

    <div class="title">
      <div class="de">Übungsbeispiele</div>
      <div class="en">Exercise Guide</div>
    </div>
  </section>

  <section class="label">
    <span class="label-name">Velvet Harbor</span>
  </section>
</div>
</body>
</html>
```